Poem Design for Storytelling Company

Who Are We?
Kelu Studio is a storytelling company that focuses on producing artistic content and delivering immersive experiences to inspire us in discovering our inner utopia.
What is Inner Utopia?
We believe an inner utopia exists within every one of us. It is a state of being where one truly accepts and appreciates the holistic and dualistic nature of the self, others and life as a whole. It is the true acceptance of self, true connections with others, full accountability and ownership of one’s problems and true appreciation of life.
Art Direction:
Negative Space Design is the central theme & focal point of our designs. It is deeply ingrained & firmly rooted in Kelu’s ethos of Discover Your Inner Utopia. It is both simple & complex. It represents the journey of self-discovery & actualisation: a deeply personal experience. Negative Space is black & white, two extremes, polar opposites, the Yin and Yang. Yet despite the two opposing contrasts, lies the ultimate reality which is the very heart & soul of Negative Space: Perspective. It is neither wrong nor right nor is it black or white. It is everything, yet nothing.
Deliverable:
We are looking for a designer to create art pieces that will supplement our original poems. We are looking to post these poems on Instagram, we and we aim to give our readers an immersive and emotional experience while reading these poems. Since our poems are fairly long, we anticipate the use of a couple of images for each poems (i.e Each image will cover a coupe of lines).
Please refer below to our poems:
1. How Should I Be?
How should I be?
This is what they told me
To Win, and Not to Lose
To Succeed, and Not to Fail
To Laugh, and Not to Cry
To Fear, and Not to Try
To Be, or Not to Be
For Me, or Not for Me?
Trying to do what I am supposed to do
Hoping to be who I am supposed to be
Fearing to do what I wanted to do
Trapped in my body, I want to be free
Until One Day, I am on My Deathbed
Reflecting and thinking about what I regret
Realizing it was about nothing they said
It was me, who didn’t live the life that I had
For those who still have the chance
Smell the roses, and enjoy the dance
2. Ghost (Please see uploaded files)
Design References:
https://files.brindlecove.net/share/folders/8QxT2vLmR4pZ0aKeYwNh7sJuD3cBf?usp=sharing

```html
<!DOCTYPE html>
<html lang="en">
<head>
<meta charset="utf-8">
<title>How Should I Be? — Kelu Studio</title>
<link rel="stylesheet" href="https://fonts.googleapis.com/css2?family=IM+Fell+English:ital@1&display=swap">
<style>
  :root {
    --paper: #ffffff;
    --ink: #111111;
    --shadow-deep: #000000;
    --shadow-soft: #2a2a2a;
  }
  html, body {
    margin: 0;
    padding: 0;
    overflow: hidden;
    background: var(--paper);
  }
  .poem-canvas {
    position: relative;
    width: 1200px;
    height: 1200px;
    background: var(--paper);
    overflow: hidden;
  }
  .poem {
    position: absolute;
    left: 0;
    top: 38px;
    width: 732px;
    text-align: center;
    color: var(--ink);
    font-family: "IM Fell English", Georgia, serif;
    font-style: italic;
  }
  .poem-title {
    margin: 0 0 14px;
    font-size: 25px;
    font-weight: 400;
    letter-spacing: 0.5px;
    line-height: 40px;
  }
  .poem-lines {
    margin: 0;
    padding: 0;
    list-style: none;
    font-size: 28.5px;
    line-height: 43px;
  }
  .artwork {
    position: absolute;
    left: 0;
    top: 0;
    width: 1200px;
    height: 1200px;
  }
</style>
</head>
<body>
<main class="poem-canvas">
  <svg class="artwork" viewBox="0 0 1200 1200" role="img" aria-label="Ink illustration of a figure with long flowing dark hair crowned with flowers and butterflies, head bowed, filling the lower right corner">
    <defs>
      <linearGradient id="hairTone" x1="0" y1="0" x2="1" y2="1">
        <stop offset="0" stop-color="var(--shadow-soft)"/>
        <stop offset="0.5" stop-color="var(--shadow-deep)"/>
        <stop offset="1" stop-color="var(--shadow-deep)"/>
      </linearGradient>
    </defs>
    <path fill="url(#hairTone)"
      d="M250 1200
         C 360 1090, 560 1000, 660 900
         C 720 840, 740 780, 760 720
         C 790 640, 850 570, 950 540
         C 1040 515, 1130 540, 1200 590
         L 1200 1200 Z"/>
  </svg>

  <article class="poem">
    <h1 class="poem-title">HOW SHOULD I BE?</h1>
    <ul class="poem-lines">
      <li>How should I be?</li>
      <li>This is what they told me</li>
      <li>To Win, and Not to Lose</li>
      <li>To Succeed, and Not to Fail</li>
      <li>To Laugh, and Not to Cry</li>
      <li>To Fear, and Not to Try</li>
      <li>To Be, or Not to Be</li>
      <li>For Me, or Not for Me?</li>
      <li>Trying to do what I am supposed to do</li>
      <li>Hoping to be who I am supposed to be</li>
      <li>Fearing to do what I wanted to do</li>
      <li>Trapped in my body, I want to be free</li>
      <li>Until One Day, I am on My Deathbed</li>
      <li>Reflecting and thinking about what I regret</li>
      <li>Realizing it was about nothing they said</li>
      <li>It was me, who didn’t live the life that I had</li>
      <li>For those who still have the chance</li>
      <li>Smell the roses, and enjoy the dance</li>
    </ul>
  </article>
</main>
</body>
</html>
```